QTV Advisory needs business card

Having just developed a logo, I now want to use that logo in the development of a business card. The card should contain the logo, my name, title, phone, email, website and physical address. I would like to use one side of the card for details and the other side for logo and messaging. Use your creativity to place the information effectively. I want the logo to appear in a strong blue, which may be matched on the back side of the card, where the logo might be reversed out in white. I want the text to be in either dark blue or black (not light blue or gray).
I am consultant, primarily helping small and mid-size companies refine their strategy, reorganize their staff and propel forward in their industry. I also teach at universities and coach on a one-on-one basis. The final design should reflect expertise, guidance, judgement, perspective, experience.
The font used in the logo is ACaslonPro.

Target Market(s)

small to mid-size companies in the US seeking business guidance

Industry/Entity Type

Business

Font styles to use
Other font styles liked:
• ACaslonPro

Colors
0455a3
0255a3
3277b5

Requirements
Must have
• Card must convey my name and information clearly. Do not make it too small - many of my customers are 50+ years old. Please use all three of my titles: Advisor / Mentor / Lecturer.
Should not have
• Please do not use icons to represent the phone, email, web. Do not use p / e / w either to indicate those details.

I have decided that a swatch of color, especially a "blue wave," does not work for me. I would rather have a simpler, more reserved look rather than a very contemporary, high color card.

Please do not deconstruct the logo or put it in a different font or italics.

```html
<!DOCTYPE html>
<html lang="en">
<head>
<meta charset="utf-8">
<title>QTV Advisory – Business Card</title>
<link rel="stylesheet" href="https://fonts.googleapis.com/css2?family=Libre+Caslon+Text:wght@400&family=Open+Sans:wght@400;600&display=swap">
<style>
  :root {
    --brand-blue: #0455a3;
    --brand-blue-deep: #0255a3;
    --brand-blue-light: #3277b5;
    --back-top: #0e5fae;
    --back-bottom: #2a86cf;
    --ink: #1c2233;
    --paper: #ffffff;
    --stage: #e9eaec;
    --rule: #0455a3;
  }
  * { box-sizing: border-box; margin: 0; padding: 0; }
  html, body {
    width: 1200px;
    height: 975px;
    overflow: hidden;
    background: var(--stage);
  }
  .stage {
    width: 1200px;
    height: 975px;
    display: flex;
    align-items: center;
    justify-content: center;
    gap: 90px;
  }
  .card {
    width: 380px;
    height: 660px;
    border-radius: 24px;
    overflow: hidden;
    box-shadow: 0 10px 30px rgba(0, 0, 0, 0.18);
    position: relative;
  }

  /* Details side */
  .card-front {
    background: var(--paper);
    display: flex;
    flex-direction: column;
  }
  .front-logo {
    height: 180px;
    display: flex;
    align-items: center;
    justify-content: center;
  }
  .wordmark {
    font-family: "Libre Caslon Text", Georgia, serif;
    font-weight: 400;
    color: var(--brand-blue);
    font-size: 38px;
    letter-spacing: 1px;
    white-space: nowrap;
  }
  .detail-row {
    flex: 1;
    display: flex;
    flex-direction: column;
    align-items: center;
    justify-content: center;
    border-top: 4px solid var(--rule);
    font-family: "Open Sans", Arial, sans-serif;
    font-size: 22px;
    line-height: 1.35;
    color: var(--ink);
    text-align: center;
  }
  .name-band {
    height: 130px;
    background: linear-gradient(90deg, var(--brand-blue) 0%, var(--brand-blue-light) 100%);
    color: var(--paper);
    font-family: "Open Sans", Arial, sans-serif;
    display: flex;
    flex-direction: column;
    justify-content: center;
    align-items: center;
    text-align: center;
  }
  .person-name {
    font-size: 23px;
    font-weight: 400;
  }
  .person-titles {
    font-size: 18px;
    margin-top: 4px;
  }

  /* Logo side */
  .card-back {
    background: linear-gradient(160deg, var(--back-top) 0%, var(--back-bottom) 100%);
    color: var(--paper);
  }
  .card-back .wordmark {
    color: var(--paper);
    font-size: 44px;
    position: absolute;
    top: 260px;
    left: 0;
    right: 0;
    text-align: center;
  }
  .back-web {
    position: absolute;
    bottom: 48px;
    left: 0;
    right: 0;
    text-align: center;
    font-family: "Open Sans", Arial, sans-serif;
    font-size: 19px;
  }
</style>
</head>
<body>
  <main class="stage">
    <section class="card card-front" aria-label="Business card, details side">
      <div class="front-logo">
        <span class="wordmark">QTV Advisory</span>
      </div>
      <div class="detail-row phone">(919) 555-0148</div>
      <div class="detail-row online">
        <span class="email">dana@qtv-advisory.com</span>
        <span class="website">www.qtv-advisory.com</span>
      </div>
      <div class="detail-row address">
        <span>2175 Larkfield Lane</span>
        <span>Raleigh, NC 27601</span>
      </div>
      <div class="name-band">
        <span class="person-name">Dana Whitfield, MBA</span>
        <span class="person-titles">Advisor / Mentor / Lecturer</span>
      </div>
    </section>

    <section class="card card-back" aria-label="Business card, logo side">
      <span class="wordmark">QTV Advisory</span>
      <span class="back-web">www.qtv-advisory.com</span>
    </section>
  </main>
</body>
</html>
```